Australia's newest tech recruitment startup

We are a new tech startup in the recruitment space.

We leverage the existing infrastructure of the recruitment network and bundle a value market based business model (like pixel flock) that appeals to business.

We are very individual, afraid of no one, minimalist, and defiantly NO "BS"!!

We're not cut price think Vellmar Auste rather than Korvani
Updates

Hey Everyone,

thanks so much for your designs. I have eliminated a lot of designs but if I havent to yours then your in with a shot. I would like to see the designs updated with a spot for our twitter handle, my blog address & our linkedIn group address. 

For some designs I think some of the above would look ok on the back of the card so not to make the front look too messy. 

thanks   

Target Market(s)

Our target market is SME's young baby boomer and Gen X

Industry/Entity Type

Business

Requirements
Must have
• Company logo, doesn't have to be both

```html
<!DOCTYPE html>
<html lang="en">
<head>
<meta charset="utf-8">
<title>Talvrenn — Business Card</title>
<link rel="stylesheet" href="https://fonts.googleapis.com/css2?family=Maven+Pro:wght@400;600&display=swap">
<style>
  :root {
    --stage: #e9e6e2;
    --card-white: #ffffff;
    --card-tint: #eef4fb;
    --brand-blue: #74b1df;
    --accent-blue: #5f86c4;
    --ink: #3a4656;
    --ink-soft: #4d5868;
    --logo-white: #ffffff;
  }
  * { box-sizing: border-box; margin: 0; padding: 0; }
  html, body {
    width: 1200px; height: 750px; overflow: hidden;
    background: var(--stage);
    font-family: "Maven Pro", sans-serif;
  }
  .canvas { position: relative; width: 1200px; height: 750px; }

  .card { position: absolute; width: 600px; height: 346px; }

  /* Back: contact side */
  .card--contact {
    left: 504px; top: 84px;
    background: linear-gradient(135deg, var(--card-tint) 0%, var(--card-white) 40%, var(--card-white) 65%, var(--card-tint) 100%);
    box-shadow: 0 2px 6px rgba(0,0,0,0.18);
  }
  .identity {
    position: absolute; right: 366px; top: 128px;
    text-align: right; color: var(--ink);
  }
  .identity__name {
    font-size: 21px; font-weight: 400; letter-spacing: 0.3px;
    padding-bottom: 2px;
    border-bottom: 2px solid var(--accent-blue);
  }
  .identity__role { font-size: 17px; margin-top: 3px; color: var(--ink-soft); }

  .divider {
    position: absolute; left: 255px; top: 80px; width: 2px; height: 168px;
    background: linear-gradient(to bottom, rgba(95,134,196,0) 0%, var(--accent-blue) 30%, var(--accent-blue) 70%, rgba(95,134,196,0) 100%);
  }

  .contact-list {
    position: absolute; left: 270px; top: 107px; list-style: none;
    color: var(--ink); font-size: 17px; line-height: 24px; letter-spacing: 0.2px;
  }
  .contact-list li { display: flex; align-items: flex-start; }
  .contact-list .icon { width: 20px; height: 24px; margin-right: 7px; flex: none; }
  .contact-list .at { color: var(--accent-blue); }

  /* Front: brand side */
  .card--brand {
    left: 103px; top: 326px;
    background: var(--brand-blue);
    box-shadow: 0 3px 8px rgba(0,0,0,0.25);
  }
  .wordmark {
    position: absolute; left: 0; right: 0; top: 110px;
    text-align: center; color: var(--logo-white);
  }
  .wordmark__name { font-size: 76px; font-weight: 600; line-height: 1; letter-spacing: -1px; }
  .wordmark__domain {
    display: block; text-align: right; width: 400px; margin: 6px auto 0;
    font-size: 14px; font-weight: 600; padding-right: 36px;
  }
</style>
</head>
<body>
<main class="canvas">

  <section class="card card--contact" aria-label="Card back with contact details">
    <div class="identity">
      <p class="identity__name">Rowan Pike</p>
      <p class="identity__role">Director</p>
    </div>
    <div class="divider"></div>
    <ul class="contact-list">
      <li>
        <svg class="icon" viewBox="0 0 20 24" aria-hidden="true">
          <circle cx="10" cy="13" r="7" fill="none" stroke="var(--accent-blue)" stroke-width="2"/>
          <circle cx="10" cy="13" r="3" fill="var(--accent-blue)"/>
        </svg>
        <span>18 Alder Lane<br>Harlow</span>
      </li>
      <li>
        <svg class="icon" viewBox="0 0 20 24" aria-hidden="true">
          <rect x="5" y="5" width="10" height="16" rx="2" fill="none" stroke="var(--accent-blue)" stroke-width="1.8"/>
          <rect x="7" y="8" width="6" height="5" fill="var(--accent-blue)"/>
          <line x1="7" y1="2" x2="7" y2="5" stroke="var(--accent-blue)" stroke-width="1.6"/>
        </svg>
        <span>104-555-0192</span>
      </li>
      <li>
        <svg class="icon" viewBox="0 0 20 24" aria-hidden="true">
          <rect x="2" y="6" width="16" height="11" fill="none" stroke="var(--accent-blue)" stroke-width="1.8"/>
          <line x1="10" y1="17" x2="10" y2="20" stroke="var(--accent-blue)" stroke-width="1.8"/>
          <line x1="6" y1="21" x2="14" y2="21" stroke="var(--accent-blue)" stroke-width="1.8"/>
        </svg>
        <span>info<span class="at">@</span>talvrenn.com</span>
      </li>
    </ul>
  </section>

  <section class="card card--brand" aria-label="Card front with company name">
    <div class="wordmark">
      <p class="wordmark__name">Talvrenn</p>
      <span class="wordmark__domain">.com.au</span>
    </div>
  </section>

</main>
</body>
</html>
```